Design a styled business card for an intimacy and attachment psychologist

I am a Psychologist providing online therapy to patients across the United States. My work is interpersonal and emotion-focused, with an emphasis on the client-therapist relationship. My primary areas of work are very personal, including sexuality and gender, abuse and trauma, and grief and loss. My target audience will be adults of all ages 18+.
My business card should convey a warm and inviting feeling of professionalism that is also casual and comfortable.
The front should be fairly simple and professional, consisting of:
- My name, Dr. Rosalind Petrakis
- My title, Licensed Psycholigist
- My logo
On either the front or the back, my contact information should be listed:
- ros@drrospetrakis.example
- 555.014.7788
- drrospetrakis.example
On the rear, I would like a description of the areas that I specialize in. This can be formatted in any way that appears stylistically interesting.
Individual and Couples
Relationships and Infidelity
Sexual Health & Aging
Gender Identity & Sexual Orientation
Abuse and Trauma
Sexual Compulsivity & Addiction
Sexual Dysfunction
Target Market(s)
My target audience will be adults of all ages 18+.
Industry/Entity Type
Psychology
Contact Information for Business Card
The front should be fairly simple and professional, consisting of: - My name, Dr. Rosalind Petrakis - My title, Licensed Psycholigist - My logo On either the front or the back, my contact information should be listed: - ros@drrospetrakis.example - 555.014.7788 - drrospetrakis.example On the rear, I would like a description of the areas that I specialize in. This can be formatted in any way that appears stylistically interesting. Individual and Couples Relationships and Infidelity Sexual Health & Aging Gender Identity & Sexual Orientation Abuse and Trauma Sexual Compulsivity & Addiction Sexual Dysfunction
- Follow brand guide

```html
<!DOCTYPE html>
<html lang="en">
<head>
<meta charset="utf-8">
<title>Dr. Rosalind Petrakis — Business Card</title>
<link rel="stylesheet" href="https://fonts.googleapis.com/css2?family=Cinzel:wght@500;600&family=Montserrat:wght@500;600&display=swap">
<style>
  :root {
    --ink: #1e1a3c;
    --teal: #9fd6cb;
    --teal-light: #cfeae4;
    --coral: #ef4a3e;
    --coral-light: #f4675a;
    --orange: #f6a21e;
    --paper: #ffffff;
    --backdrop: #e9eaec;
  }
  * { margin: 0; padding: 0; box-sizing: border-box; }
  html, body { width: 1200px; height: 880px; overflow: hidden; background: var(--backdrop); }
  .canvas { position: relative; width: 1200px; height: 880px; }
  .card {
    position: absolute; left: 250px; width: 700px; height: 400px;
    background: var(--paper); overflow: hidden;
    box-shadow: 0 6px 22px rgba(0,0,0,.18);
    color: var(--ink);
  }
  .card--specialties { top: 30px; }
  .card--contact { top: 450px; }
  .card-art { position: absolute; inset: 0; }
  .brand-name {
    position: absolute; font-family: "Cinzel", serif; font-weight: 600;
    color: var(--ink); line-height: 1.02; letter-spacing: 1px;
  }
  .brand-name .small { font-size: 20px; display: block; }
  .brand-name .big { font-size: 32px; display: block; }
  .divider { position: absolute; left: 300px; top: 110px; width: 1.5px; height: 220px; background: var(--ink); }
  .specialties { position: absolute; left: 322px; top: 92px; }
  .specialties-title { font-family: "Cinzel", serif; font-weight: 600; font-size: 22px; letter-spacing: 1px; margin-bottom: 8px; }
  .specialties-list { list-style: none; font-family: "Montserrat", sans-serif; font-weight: 500; font-size: 14px; }
  .specialties-list li { position: relative; padding-left: 20px; line-height: 24px; white-space: nowrap; }
  .specialties-list li::before {
    content: ""; position: absolute; left: 2px; top: 8px; width: 9px; height: 9px;
    border-radius: 50%; background: var(--orange);
  }
  .person { position: absolute; left: 60px; top: 230px; font-family: "Cinzel", serif; font-weight: 600; }
  .person-name { font-size: 28px; letter-spacing: .5px; }
  .person-title { font-size: 18px; letter-spacing: 1px; }
  .contacts { position: absolute; left: 60px; top: 305px; list-style: none; font-family: "Montserrat", sans-serif; font-weight: 500; font-size: 16px; }
  .contacts li { display: flex; align-items: center; gap: 10px; height: 26px; }
  .contacts .phone-number { font-weight: 600; font-size: 18px; }
  .contact-icon { width: 20px; height: 20px; flex: none; }
</style>
</head>
<body>
<main class="canvas">

  <section class="card card--specialties" aria-label="Card back: specialties">
    <svg class="card-art" viewBox="0 0 700 400" aria-hidden="true">
      <path d="M0,0 H300 C265,55 240,110 222,155 C200,210 110,200 0,190 Z" fill="var(--teal)" stroke="var(--ink)" stroke-width="3"/>
      <path d="M0,0 H150 C115,40 85,100 0,130 Z" fill="var(--teal-light)" opacity=".6"/>
      <path d="M700,110 C675,112 665,170 658,230 C652,290 668,330 700,332 Z" fill="var(--coral)" stroke="var(--ink)" stroke-width="3"/>
      <path d="M700,135 C685,140 680,185 677,230 C675,270 685,290 700,295 Z" fill="var(--coral-light)"/>
      <circle cx="150" cy="205" r="42" fill="var(--teal-light)" stroke="var(--ink)" stroke-width="3"/>
    </svg>
    <div class="brand-name" style="left:60px; top:268px;">
      <span class="small">Dr.</span>
      <span class="big">Rosalind<br>Petrakis</span>
    </div>
    <div class="divider"></div>
    <div class="specialties">
      <h2 class="specialties-title">Specialize In</h2>
      <ul class="specialties-list">
        <li>Individual and Couples</li>
        <li>Relationships and Infidelity</li>
        <li>Sexual Health &amp; Aging</li>
        <li>Gender Identity &amp; Sexual Orientation</li>
        <li>Abuse and Trauma</li>
        <li>Sexual Compulsivity &amp; Addiction</li>
        <li>Sexual Dysfunction</li>
      </ul>
    </div>
  </section>

  <section class="card card--contact" aria-label="Card front: name and contact">
    <svg class="card-art" viewBox="0 0 700 400">
      <defs>
        <linearGradient id="featureTone" x1="0" y1="0" x2="1" y2="1">
          <stop offset="0" stop-color="#9fd6cb"/>
          <stop offset=".6" stop-color="#cfeae4"/>
          <stop offset="1" stop-color="#f7c27a"/>
        </linearGradient>
      </defs>
      <g role="img" aria-label="Large decorative brand illustration area">
        <path d="M380,0 H700 V270 C640,330 560,320 520,250 C485,190 430,150 395,95 C385,60 380,30 380,0 Z" fill="url(#featureTone)" stroke="var(--ink)" stroke-width="4"/>
      </g>
      <circle cx="95" cy="105" r="40" fill="var(--teal-light)" stroke="var(--ink)" stroke-width="3"/>
    </svg>
    <div class="brand-name" style="left:150px; top:62px;">
      <span class="small">Dr.</span>
      <span class="big">Rosalind<br>Petrakis</span>
    </div>
    <div class="person">
      <p class="person-name">Dr. Rosalind Petrakis</p>
      <p class="person-title">Licensed Psychologist</p>
    </div>
    <ul class="contacts">
      <li>
        <svg class="contact-icon" viewBox="0 0 20 20" aria-hidden="true"><circle cx="10" cy="10" r="9" fill="var(--orange)" stroke="var(--ink)" stroke-width="1.5"/><path d="M7 5.5l2 2-1 1.2c.6 1.3 1.6 2.3 2.9 2.9l1.2-1 2 2-1.2 1.5C9.5 14 6 10.5 5.9 6.6Z" fill="#fff"/></svg>
        <span class="phone-number">555.014.7788</span>
      </li>
      <li>
        <svg class="contact-icon" viewBox="0 0 20 20" aria-hidden="true"><circle cx="10" cy="10" r="9" fill="var(--teal)" stroke="var(--ink)" stroke-width="1.5"/><rect x="5.5" y="7" width="9" height="6.5" fill="#fff"/><path d="M5.5 7l4.5 3.5L14.5 7" fill="none" stroke="var(--teal)" stroke-width="1"/></svg>
        <span>ros@drrospetrakis.example</span>
      </li>
      <li>
        <svg class="contact-icon" viewBox="0 0 20 20" aria-hidden="true"><circle cx="10" cy="10" r="9" fill="var(--coral)" stroke="var(--ink)" stroke-width="1.5"/><circle cx="10" cy="10" r="5" fill="none" stroke="#fff" stroke-width="1.2"/><path d="M5 10h10M10 5c-2 3-2 7 0 10M10 5c2 3 2 7 0 10" fill="none" stroke="#fff" stroke-width="1"/></svg>
        <span>drrospetrakis.example</span>
      </li>
    </ul>
  </section>

</main>
</body>
</html>
```